Slick Facebook Ad

We've recently re-branded our business to reflect our ethos "Wealth is about more than money - it's about choice." We aim to protect your hard-earned success and help achieve your lifestyle aspirations, whether that's retiring at fifty to go globetrotting, or buying your first home. We're a financial consultancy that primarily services high-net-worth clients.

Our brand is minimalist, modern (check out our website) and the brief focuses on our strong investment return for the past 12 years.

Task: The attached brief is for a Facebook advertisement. Please see competitor images as a guide to how 'returns' and 'branding' can both be displayed in a design.

Target Market(s)

+30

Font styles to use
Sans Serif

Requirements
Must have
• Creative should feature the strong investment return, and design aesthetic should be 'on-brand' (modern, minimalist, lifestyle focused).

```html
<!DOCTYPE html>
<html lang="en">
<head>
<meta charset="UTF-8">
<title>Linden Wealth – Portfolio Returns Ad</title>
<link rel="stylesheet" href="https://fonts.googleapis.com/css2?family=Mulish:wght@600;800&display=swap">
<style>
  :root {
    --canvas: #ffffff;
    --olive: #a2b21c;
    --bottle-dark: #0c0b0a;
    --bottle-mid: #2a2622;
    --bottle-glint: #4a4438;
  }
  html, body {
    margin: 0;
    padding: 0;
    width: 1200px;
    height: 1200px;
    overflow: hidden;
    background: var(--canvas);
  }
  .canvas {
    position: relative;
    width: 1200px;
    height: 1200px;
    background: var(--canvas);
    font-family: "Mulish", sans-serif;
  }
  .ad-banner {
    position: absolute;
    left: 51px;
    top: 317px;
    width: 1098px;
    height: 566px;
    overflow: hidden;
  }
  .ad-photo {
    position: absolute;
    inset: 0;
    background:
      radial-gradient(ellipse 30% 60% at 20% 40%, rgba(90,80,65,0.55), transparent 70%),
      radial-gradient(ellipse 20% 50% at 90% 20%, rgba(120,105,70,0.35), transparent 70%),
      linear-gradient(90deg, var(--bottle-mid) 0%, var(--bottle-glint) 18%, var(--bottle-dark) 45%, var(--bottle-dark) 70%, var(--bottle-mid) 100%);
  }
  .brand {
    position: absolute;
    top: 128px;
    left: 0;
    width: 100%;
    display: flex;
    justify-content: center;
    align-items: center;
    gap: 12px;
    color: var(--olive);
    font-weight: 800;
    font-size: 28px;
    letter-spacing: 0.5px;
  }
  .brand-dot {
    width: 22px;
    height: 22px;
    border-radius: 50%;
    background: var(--olive);
  }
  .headline {
    position: absolute;
    top: 232px;
    left: 0;
    width: 100%;
    margin: 0;
    text-align: center;
    color: var(--olive);
    font-weight: 600;
    font-size: 32px;
    line-height: 44px;
  }
  .headline strong {
    font-weight: 800;
  }
</style>
</head>
<body>
  <div class="canvas">
    <section class="ad-banner">
      <div class="ad-photo" role="img" aria-label="Close-up photo of a row of dark wine bottles in low light"></div>
      <div class="brand"><span class="brand-dot"></span><span>Linden Wealth</span></div>
      <p class="headline">Our global investment portfolio delivered<br><strong>20.5% returns</strong> over the past 12 months.</p>
    </section>
  </div>
</body>
</html>
```